Buch-/E-Book-Cover für Schriftstellerin
Vielen Dank für das schöne Cover zu meiner Kurzgeschichtensammlung!
Zielgruppe
30-jährige Schriftstellerin (Kurzgeschichten, Roman in Arbeit, Gedichte)
Zielgruppe der Kurzgeschichtensammlung 'Sesselsturm': 17-50 Jährige Kurzgeschichten-Leser (alle Geschlechter), Tomeo Kasagawa-, Brackfield-, Velsch-Leser, Hobby-Philosophen, Intellektuelle, Melancholiker
Klappentext:
„Miese Gedanken sind der Isolierstoff zwischen mir und meiner Umwelt.“
Eine Frau geht in ihrer Badewanne an Bord eines Papierschiffs, ein Paar wandert über Möbel und ein Mann, dessen Name sich keiner merken kann, spricht von der Couch aus mit seinen Bücherschränken...
„Sesselsturm“ nähert sich dem modernen Menschen auf einfühlsame wie humoristische Weise. Psychologisch, verträumt, surreal und wohltuend melancholisch - in 14 Kurzgeschichten treffen Personen und Mobiliar, Seelenraum und Außenwelt, Pandemie und Heavy Metal aufeinander.
Aufgabenstellung
Design passend zum Titel 'Sesselsturm'. In meiner Geschichte ist das Sesselsturm der Moment, in dem der depressive und angstgeplagte Protagonist auf der Couch liegt und sich das Chaos vorstellt, das er anrichten würde, wenn er die Möbel auf den Kopf stellen würde, sodass die Schubladen der Schränke keinen Sinn mehr ergäben oder er seinen Körper aufschneiden würde. Die Geschichte hat ein Happy End und er wird gesund. Es ist nur ein kurzer Moment der Depression. Die 14 Kurzgeschichten sind nachenklich, ehrlich, aber auch stellenweise lustig sowie surreal.
Das Cover soll farbenfroh sein und mit serifenloser Schrift, abstrakt-künstlerisch und modern. Bitte keine Fotos von 'realen' Menschen.
Titel: Sesselsturm (kann auch großgeschrieben sein)
Untertitel: 14 Kurzgeschichten
Autorin: Theresa Lindl
Ansonsten keine Vorgaben.

```html
<!DOCTYPE html>
<html lang="de">
<head>
<meta charset="utf-8">
<title>Sesselsturm – Theresa Lindl</title>
<link rel="stylesheet" href="https://fonts.googleapis.com/css2?family=Rubik+Dirt&family=Oswald:wght@300;500&family=Pathway+Gothic+One&display=swap">
<style>
  :root {
    --teal-deep: #12403f;
    --teal-mid: #2f7f80;
    --teal-light: #5fb3b0;
    --sand: #c9d6d8;
    --sand-pale: #e3eaec;
    --couch: #a8849a;
    --couch-dark: #7d5f72;
    --band: rgba(70, 74, 84, 0.42);
    --ink: #f4f5fa;
  }
  * { margin: 0; padding: 0; box-sizing: border-box; }
  html, body { width: 837px; height: 1200px; overflow: hidden; background: #ffffff; }
  .cover {
    position: relative;
    width: 837px;
    height: 1200px;
    overflow: hidden;
  }
  .cover__scene {
    position: absolute;
    inset: 0;
    background: linear-gradient(180deg,
      var(--teal-deep) 0%,
      var(--teal-mid) 22%,
      var(--teal-light) 45%,
      #4e8f92 58%,
      var(--sand) 78%,
      var(--sand-pale) 100%);
  }
  .cover__couch {
    position: absolute;
    left: 178px;
    top: 600px;
    width: 640px;
    height: 250px;
    border-radius: 40px 40px 14px 14px;
    background: linear-gradient(180deg, var(--couch) 0%, var(--couch-dark) 100%);
    opacity: 0.9;
  }
  .cover__band {
    position: absolute;
    left: 242px;
    top: 0;
    width: 396px;
    height: 1200px;
    background: var(--band);
  }
  .cover__title {
    position: absolute;
    left: 0;
    right: 0;
    top: 40px;
    text-align: center;
    font-family: "Rubik Dirt", sans-serif;
    font-weight: 400;
    font-size: 150px;
    line-height: 200px;
    color: var(--ink);
    letter-spacing: 2px;
  }
  .cover__title span {
    display: block;
    transform: scaleY(1.35);
  }
  .cover__subtitle {
    position: absolute;
    left: 275px;
    top: 492px;
    font-family: "Oswald", sans-serif;
    font-weight: 500;
    font-size: 34px;
    letter-spacing: 1.5px;
    color: var(--ink);
  }
  .cover__tagline {
    position: absolute;
    right: 232px;
    top: 868px;
    text-align: right;
    font-family: "Oswald", sans-serif;
    font-weight: 300;
    color: var(--ink);
    line-height: 1;
  }
  .cover__tagline .big { display: block; font-size: 56px; margin-bottom: 6px; }
  .cover__tagline .small { display: block; font-size: 42px; margin-bottom: 8px; letter-spacing: -0.5px; }
  .cover__author {
    position: absolute;
    left: 242px;
    width: 396px;
    top: 1108px;
    text-align: center;
    font-family: "Pathway Gothic One", sans-serif;
    font-size: 34px;
    letter-spacing: 1px;
    color: var(--ink);
  }
</style>
</head>
<body>
  <div class="cover">
    <div class="cover__scene" role="img" aria-label="Surreale Unterwasserszene: überflutetes Wohnzimmer mit schwebenden Stühlen, Geschirr, Schachbrett, Korb und Goldfischen über sandigem Boden"></div>
    <div class="cover__couch" role="img" aria-label="Altrosa Sofa mit Kissen auf dem Meeresgrund"></div>
    <div class="cover__band"></div>

    <h1 class="cover__title"><span>SESSEL</span><span>STURM</span></h1>
    <p class="cover__subtitle">14 Kurzgeschichten</p>

    <p class="cover__tagline">
      <span class="big">Miese Gedanken</span>
      <span class="small">sind der Isolierstoff</span>
      <span class="big">zwischen mir</span>
      <span class="small">und meiner Umwelt</span>
    </p>

    <p class="cover__author">Theresa Lindl</p>
  </div>
</body>
</html>
```